IT Consulting Business Card Design

We need a business card on our company name....which is a IT consulting and staffing company. We also train masters graduates in various IT courses. 70% of the time these cards will be handed out to the graduate students at the universities. 30% for our clients and business partners. We are uploading our company logo...would like to see something that matches our logo or blends with it. Please visit www.brightvaleworks.com for more details on logo and colors.

Target Market(s)

70% of the time these cards will be handed out to the graduate students at the universities. 30% for our clients and business partners.

Industry/Entity Type

Business

Contact Information for Business Card

Ravi Kondamuri
Vice-President
Bright Vale Works Inc
3807 Morrow Lane, Suite 412
East Brookridge, NJ 07315
ravi@brightvaleworks.com
Office : 1-866-219-3840 X 515
Cell number : 732-581-9034

Requirements
Nice to have
• may be company logo and name on the back of the card and detials on the other side...just a thought..!!

```html
<!DOCTYPE html>
<html lang="en">
<head>
<meta charset="utf-8">
<title>Bright Vale Works – Business Card</title>
<link rel="stylesheet" href="https://fonts.googleapis.com/css2?family=PT+Sans+Narrow:wght@700&family=PT+Sans:wght@400;700&display=swap">
<style>
  :root {
    --page: #f2f2f2;
    --carbon-dark: #1f2022;
    --carbon-light: #3a3b3e;
    --brand-red: #d71f26;
    --paper: #ffffff;
    --ink-light: #f4f4f4;
    --ink-muted: #c9c9c9;
  }
  * { box-sizing: border-box; margin: 0; padding: 0; }
  html, body { width: 1200px; height: 900px; overflow: hidden; }
  body {
    background: var(--page);
    font-family: "PT Sans", Arial, sans-serif;
    position: relative;
  }
  .card {
    position: absolute;
    top: 300px;
    width: 525px;
    height: 300px;
    border-radius: 18px;
    overflow: hidden;
    background: radial-gradient(ellipse at 30% 30%, var(--carbon-light), var(--carbon-dark) 75%);
    box-shadow: 0 10px 24px rgba(0,0,0,0.18);
  }
  .card--front { left: 50px; }
  .card--back { left: 625px; }

  .front-shape { position: absolute; inset: 0; width: 100%; height: 100%; }

  .company-name {
    font-family: "PT Sans Narrow", "Arial Narrow", sans-serif;
    font-weight: 700;
    color: var(--ink-light);
    letter-spacing: 0.5px;
    white-space: nowrap;
  }
  .card--front .company-name {
    position: absolute; left: 26px; top: 34px; font-size: 27px;
  }
  .holder { position: absolute; left: 26px; top: 118px; }
  .holder-name { color: var(--brand-red); font-weight: 700; font-size: 16px; }
  .holder-title { color: var(--ink-light); font-size: 12px; margin-top: 1px; }

  .contact-list {
    position: absolute; left: 26px; top: 178px;
    list-style: none; color: var(--ink-light); font-size: 14px; line-height: 19px;
  }
  .contact-list li { display: flex; align-items: flex-start; gap: 6px; }
  .contact-list svg { width: 12px; height: 12px; margin-top: 3px; flex: none; fill: var(--brand-red); }
  .contact-list .address-line { padding-left: 18px; }

  .brand-lockup {
    position: absolute; left: 36px; top: 102px;
    display: flex; align-items: center; gap: 18px;
  }
  .brand-dot {
    width: 96px; height: 96px; border-radius: 50%;
    background: var(--brand-red);
  }
  .card--back .company-name { font-size: 40px; }
  .website {
    position: absolute; left: 0; right: 0; bottom: 40px;
    text-align: center; color: var(--ink-light);
    font-size: 19px; letter-spacing: 6px;
  }
</style>
</head>
<body>

<section class="card card--front" aria-label="Card front with contact details">
  <svg class="front-shape" viewBox="0 0 525 300" aria-hidden="true">
    <path d="M246,0 Q196,150 290,300 L525,300 L525,0 Z" fill="var(--paper)"/>
    <path d="M226,0 L304,0 Q236,70 232,200 Q204,110 226,0 Z" fill="var(--brand-red)"/>
  </svg>

  <div class="company-name">BRIGHT VALE WORKS</div>

  <div class="holder">
    <div class="holder-name">Ravi Kondamuri</div>
    <div class="holder-title">Vice-President</div>
  </div>

  <ul class="contact-list">
    <li>
      <svg viewBox="0 0 12 12"><path d="M2.5 0.5l2 2.4-1.1 1.5c.8 1.6 2 2.8 3.6 3.6l1.5-1.1 2.4 2-1.2 2.1C4.8 10.6 1.4 7.2.4 2.7z"/></svg>
      1-866-219-3840 X 515
    </li>
    <li>
      <svg viewBox="0 0 12 12"><path d="M3 0h6v12H3zM4 1.5v7.5h4V1.5z"/></svg>
      732-581-9034
    </li>
    <li>
      <svg viewBox="0 0 12 12"><path d="M0 2h12v8H0zM1 3l5 3.6L11 3v-.1H1z"/></svg>
      ravi@brightvaleworks.com
    </li>
    <li>
      <svg viewBox="0 0 12 12"><path d="M6 0.5L0 6h2v5.5h3V8h2v3.5h3V6h2z"/></svg>
      3807 Morrow Lane,
    </li>
    <li class="address-line">Suite 412 East Brookridge, NJ 07315</li>
  </ul>
</section>

<section class="card card--back" aria-label="Card back with company name">
  <div class="brand-lockup">
    <span class="brand-dot"></span>
    <span class="company-name">BRIGHT VALE WORKS</span>
  </div>
  <div class="website">www.brightvaleworks.com</div>
</section>

</body>
</html>
```